Business card design needed

I need a business card that sets my business apart from big gyms and intimidating personal trainers. My personal training business focuses on outdoor and client in-home training, in an environment that is both enjoyable and sustainable for the client.
I train males and females, however a large proportion of my clientelle are female, so I would like the card to lean towards females, but still have a bit of masculine appeal about it.
My business colours are a deep sky blue and lightish red/orange (as seen in logo)

Contact Information for Business Card

Your Health & Fitness Mentor
Discover a happier, healthier you!
Benedict Rowlan- Health and Fitness Professional
Locations all across the Yarra Valley and Eastern Suburbs of Melbourne
0438152906
benedictrowlanpt@mailora.com.au

Requirements
Must have
• - Mobile number must stand out
- The 'Locations all across the Yarra Valley and Eastern Suburbs of Melbourne' must be clear and easy to read (different colour maybe?)

```html
<!DOCTYPE html>
<html lang="en">
<head>
<meta charset="utf-8">
<title>Benedict Rowlan – Business Card</title>
<link rel="stylesheet" href="https://fonts.googleapis.com/css2?family=Share+Tech+Mono&display=swap">
<style>
  :root {
    --stage-top: #55554f;
    --stage-bottom: #7c7c74;
    --card-white: #ffffff;
    --ink-orange: #ef5a2a;
    --orange-deep: #e8461f;
    --orange-light: #f7885a;
    --sky-blue: #1f80c4;
    --faint: #efefef;
    --card-font: "Share Tech Mono", monospace;
  }
  * { box-sizing: border-box; margin: 0; padding: 0; }
  html, body { width: 1200px; height: 675px; overflow: hidden; }
  body {
    background: radial-gradient(ellipse at 70% 80%, var(--stage-bottom), var(--stage-top));
    font-family: var(--card-font);
    position: relative;
  }
  .card {
    position: absolute;
    top: 192px;
    width: 500px;
    height: 290px;
    border-radius: 10px;
    box-shadow: 0 8px 20px rgba(0,0,0,0.35);
    overflow: hidden;
    font-variant: small-caps;
  }
  .card-front { left: 70px; background: var(--card-white); }
  .card-back {
    left: 630px;
    background: radial-gradient(circle at 50% 45%, var(--orange-light), var(--ink-orange) 55%, var(--orange-deep));
    color: var(--card-white);
    text-align: center;
  }
  .front-watermark {
    position: absolute;
    top: 18px;
    right: -20px;
    font-size: 78px;
    color: var(--faint);
    letter-spacing: 2px;
    white-space: nowrap;
  }
  .front-details {
    position: absolute;
    left: 22px;
    top: 104px;
    color: var(--ink-orange);
  }
  .name-marker {
    position: absolute;
    left: 0;
    top: 108px;
    width: 4px;
    height: 26px;
    background: var(--ink-orange);
  }
  .holder-name { font-size: 24px; letter-spacing: 2px; line-height: 1.1; }
  .holder-role { font-size: 13px; letter-spacing: 1px; margin-bottom: 18px; }
  .service-area { font-size: 13px; line-height: 1.35; letter-spacing: 0.5px; margin-bottom: 2px; }
  .contact-line { font-size: 13px; line-height: 1.35; letter-spacing: 0.5px; }
  .contact-line.phone { font-size: 15px; }
  .brand-lockup {
    position: absolute;
    top: 62px;
    left: 0;
    right: 0;
    display: flex;
    align-items: center;
    justify-content: center;
    gap: 12px;
  }
  .brand-name { font-size: 28px; letter-spacing: 2px; color: var(--card-white); }
  .back-tagline {
    position: absolute;
    left: 0;
    right: 0;
    top: 182px;
    line-height: 1.3;
    letter-spacing: 1px;
  }
  .back-tagline .headline { font-size: 19px; }
  .back-tagline .subline { font-size: 16px; }
</style>
</head>
<body>
  <section class="card card-front">
    <div class="front-watermark" aria-hidden="true">Rowlan PT</div>
    <span class="name-marker"></span>
    <div class="front-details">
      <h1 class="holder-name">Benedict Rowlan</h1>
      <p class="holder-role">Health and Fitness Professional</p>
      <p class="service-area">The Location<br>All across the Yarra Valley and<br>Eastern Suburbs of Melbourne</p>
      <p class="contact-line phone">p. 0438152906</p>
      <p class="contact-line">e. benedictrowlanpt@mailora.com.au</p>
    </div>
  </section>

  <section class="card card-back">
    <div class="brand-lockup">
      <svg width="46" height="46" viewBox="0 0 46 46" aria-hidden="true">
        <circle cx="23" cy="23" r="20" fill="none" stroke="#1f80c4" stroke-width="4"/>
      </svg>
      <span class="brand-name">Rowlan PT</span>
    </div>
    <div class="back-tagline">
      <p class="headline">Your Health &amp; Fitness Mentor</p>
      <p class="subline">Discover a happier, healthier you!</p>
    </div>
  </section>
</body>
</html>
```